Business Card Design & logo

Residential building renovation and maintenance work.
All carpentry and joinery needs.
Laying solid timber and floating floors.
Kitchen and bathroom makeovers and modifications.
Interior fitouts,
small job specialist. tiling, plastering, painting,

I would like a silver background. With the use of different shades of grey, rustic orange, black and white.
I do not want pictures of hammers, chisels etc. I am looking for a logo to be incorporated into the card.

Industry/Entity Type

Carpentry

Contact Information for Business Card

BTW Renovations and Maintenance
Lionel Pasquet
0471526083
info@btwrefits.com.au
btwrefits.com.au

```html
<!DOCTYPE html>
<html lang="en">
<head>
<meta charset="utf-8">
<title>BTW Renovations and Maintenance – Business Card</title>
<link rel="stylesheet" href="https://fonts.googleapis.com/css2?family=Alegreya:wght@400&family=Lato:wght@400&display=swap">
<style>
  :root {
    --page: #d9d6d2;
    --card: #050505;
    --orange: #f08a24;
    --silver: #c9c9c9;
    --grey-text: #bdbdbd;
    --white: #f2f2f2;
    --faint: #1c1c1c;
    --divider: #3a3a3a;
  }
  * { margin: 0; padding: 0; box-sizing: border-box; }
  html, body { width: 1200px; height: 900px; overflow: hidden; }
  body { background: var(--page); position: relative; }

  .card {
    position: absolute;
    width: 620px;
    height: 354px;
    background: var(--card);
    border-radius: 3px;
    box-shadow: 0 10px 28px rgba(0,0,0,0.28);
    overflow: hidden;
  }
  .card--services { left: 70px; top: 110px; }
  .card--contact { left: 520px; top: 430px; }

  /* brand mark stand-in */
  .brand {
    position: absolute;
    display: flex;
    align-items: center;
    gap: 12px;
    font-family: "Alegreya", serif;
    font-weight: 400;
    color: var(--silver);
  }
  .brand__dot {
    width: 22px; height: 22px;
    border-radius: 50%;
    background: var(--orange);
    flex: none;
  }
  .card--services .brand { left: 0; right: 0; top: 50px; justify-content: center; font-size: 46px; letter-spacing: 4px; }

  .services {
    position: absolute;
    left: 30px; right: 30px; top: 190px;
    display: grid;
    grid-template-columns: 1fr 1fr;
    font-family: "Lato", sans-serif;
    font-size: 14.5px;
    line-height: 1.45;
    color: var(--grey-text);
  }
  .services__col--left { text-align: right; padding: 18px 18px 0 0; border-right: 1px solid var(--divider); }
  .services__col--right { text-align: left; padding: 0 0 0 18px; }

  /* front */
  .watermark {
    position: absolute;
    right: -20px; top: 10px;
    font-family: "Alegreya", serif;
    font-size: 150px;
    color: var(--faint);
    line-height: 1;
  }
  .card--contact .brand {
    left: 90px; top: 110px;
    font-size: 27px;
    color: var(--white);
  }
  .person {
    position: absolute;
    left: 250px; top: 172px;
    font-family: "Alegreya", serif;
  }
  .person__name { color: var(--orange); font-size: 25px; line-height: 1.1; }
  .person__role { color: var(--white); font-size: 15px; margin-top: 2px; }
  .contact-list {
    list-style: none;
    margin-top: 18px;
    font-size: 15px;
    line-height: 1.5;
    color: var(--white);
  }
  .contact-list__label { color: var(--orange); }
</style>
</head>
<body>

  <section class="card card--services" aria-label="Business card, services side">
    <div class="brand"><span class="brand__dot"></span>BTW</div>
    <div class="services">
      <p class="services__col services__col--left">
        Residential building renovation<br>and maintenance work.<br>
        All carpentry and joinery needs.<br>Laying solid timber and floating floors.
      </p>
      <p class="services__col services__col--right">
        Kitchen and bathroom makeovers<br>and modifications.<br>
        Interior fitouts, small job specialist.<br>Tiling, plastering, painting.
      </p>
    </div>
  </section>

  <section class="card card--contact" aria-label="Business card, contact side">
    <div class="watermark" aria-hidden="true">BTW</div>
    <div class="brand"><span class="brand__dot"></span>BTW Renovations and Maintenance</div>
    <div class="person">
      <p class="person__name">Lionel Pasquet</p>
      <p class="person__role">Owner</p>
      <ul class="contact-list">
        <li><span class="contact-list__label">T:</span> 0471526083</li>
        <li><span class="contact-list__label">E:</span> info@btwrefits.com.au</li>
        <li><span class="contact-list__label">W:</span> www.btwrefits.com.au</li>
      </ul>
    </div>
  </section>

</body>
</html>
```